Brisa Home Residential cleaning services- Opening Flyer

1. I would like to have flyer design offering the hourly rate residential cleaning normal rate will be 35 AED per hour.
2. I want to have a special opening rate which is less than 25 AED which is equivalent to 30% Off.This opening offer will be limited time
We have a different cleaning packages like "Basic , Deep, And custom"
3. Also we have different types contracts Yearly/Monthly/Weekly and daily.
4. we are providing cleaning material and cleaning equipment upon request.And all the material used are environmental friendly.
5. Our customers mostly will be house wives.
6. Our service will be available in Ruwais city.
7. I would like to have a modern attractive flyer, i like it to be smart in its colors and the psychology of the customers.
8. I like to have attractive statements like " Now Available in Ruwais" and other statements from your own.
9. I will attach my logo design and if you need any other uploads let me know.
10. Our slogan is "Experience the Difference"
11. Paper size , i expect to be A5 (210mm x 148mm).
12. I am expecting the flyer to be single size as it will translated to another language in the other side.
13. please use the statement also ( less than 25 AED)
14. Do the arrangement you can see to the flyer statements as to look professional and comfortable to read.
15. Company web site is " www.brisahome.ae"
16. company email " support@brisahome.ae"
17. I will update you with contact number soon
18. My contacts are
Support@brisahome.ae
+971 508817394
+971 508817396
19. Update some slogans to be used
Industry/Entity Type
Residential
Look and feel
Each slider illustrates characteristics of the customer's brand and the style your logo design should communicate.

```html
<!DOCTYPE html>
<html lang="en">
<head>
<meta charset="utf-8">
<title>Brisa Home – Opening Flyer</title>
<link href="https://fonts.googleapis.com/css2?family=Montserrat:wght@400;600;700;800&family=Quicksand:wght@400;500;600&display=swap" rel="stylesheet">
<style>
  :root{
    --page:#e4e4e6;
    --paper-top:#f7f7f8;
    --paper-bottom:#dcdcdf;
    --brand-blue:#1f6db3;
    --deep-blue:#154f8e;
    --text-blue:#2a7fc1;
    --teal:#1aa3a0;
    --lime:#8cc63f;
    --grey-text:#5a5a5e;
    --white:#ffffff;
  }
  *{box-sizing:border-box;margin:0;padding:0}
  html,body{width:1200px;height:1000px;overflow:hidden}
  body{background:var(--page);position:relative;font-family:'Quicksand',sans-serif}
  .flyer{
    position:absolute;left:100px;top:147px;width:1000px;height:705px;
    background:linear-gradient(180deg,var(--paper-top) 0%,#eeeef0 55%,var(--paper-bottom) 100%);
    box-shadow:0 18px 40px rgba(0,0,0,.18);overflow:hidden;
  }
  .fold{position:absolute;left:0;right:0;height:2px;background:linear-gradient(180deg,rgba(0,0,0,.06),rgba(255,255,255,.8))}
  .fold--upper{top:235px}
  .fold--lower{top:470px}
  .headline{
    position:absolute;left:70px;top:46px;
    font-family:'Montserrat',sans-serif;font-weight:800;font-size:40px;line-height:1.02;
    color:var(--brand-blue);text-transform:uppercase;letter-spacing:.5px;
  }
  .tagline{
    position:absolute;left:70px;top:140px;font-size:26px;font-weight:500;
    color:var(--teal);letter-spacing:2px;
  }
  .rule-dotted{position:absolute;border:0 dashed var(--teal)}
  .rule-dotted--tag{left:70px;top:182px;width:500px;border-top-width:2px}
  .rule-dotted--drop{left:570px;top:182px;height:120px;border-left-width:2px}
  .rule-dotted--slogan{left:70px;top:410px;width:470px;border-top-width:2px}
  .services{
    position:absolute;left:86px;top:200px;width:450px;
    list-style:disc;color:var(--text-blue);font-size:16px;font-weight:500;line-height:1.3;
  }
  .statement{
    position:absolute;left:70px;top:352px;font-size:34px;font-weight:500;color:var(--grey-text);
  }
  .slogan{
    position:absolute;left:300px;top:420px;width:240px;text-align:right;
    font-family:'Montserrat',sans-serif;font-weight:700;font-size:19px;color:var(--grey-text);
  }
  .disclaimer{
    position:absolute;left:70px;top:424px;font-size:11px;font-style:italic;color:var(--text-blue);
  }
  .address{
    position:absolute;left:70px;top:446px;display:flex;align-items:center;gap:10px;
    font-size:26px;font-weight:500;color:var(--grey-text);
  }
  .phone{
    position:absolute;left:60px;top:496px;width:380px;height:70px;border-radius:35px;
    background:var(--brand-blue);display:flex;align-items:center;gap:16px;padding-left:10px;
    font-family:'Montserrat',sans-serif;font-weight:600;font-size:42px;color:var(--white);letter-spacing:2px;
  }
  .phone__icon{width:52px;height:52px;border-radius:50%;background:var(--white);display:flex;align-items:center;justify-content:center}
  .phone-line{position:absolute;left:440px;top:530px;width:300px;height:2px;background:var(--brand-blue)}
  .duster{
    position:absolute;left:560px;top:230px;width:230px;height:320px;border-radius:40% 40% 45% 45%/20% 20% 60% 60%;
    background:radial-gradient(ellipse at 50% 75%,#6f665c 0%,#4d463f 55%,#9a9a9c 100%);
  }
  .offer-badge{position:absolute;left:700px;top:90px;width:320px;height:320px}
  .brand-mark{
    position:absolute;left:620px;top:590px;display:flex;align-items:center;gap:14px;
    font-family:'Montserrat',sans-serif;font-weight:700;font-size:44px;color:var(--brand-blue);
  }
  .brand-mark__dot{width:34px;height:34px;border-radius:50%;background:var(--lime)}
</style>
</head>
<body>
<main class="flyer">
  <div class="fold fold--upper"></div>
  <div class="fold fold--lower"></div>

  <h1 class="headline">The Cleaning Company<br>You Search For</h1>
  <p class="tagline">Now Available in Ruwais</p>
  <div class="rule-dotted rule-dotted--tag"></div>
  <div class="rule-dotted rule-dotted--drop"></div>

  <ul class="services">
    <li>We have a different cleaning packages like "Basic , Deep, And custom"</li>
    <li>We have different types contracts Yearly/Monthly/Weekly and daily.</li>
    <li>We are providing cleaning material and cleaning equipment upon request.</li>
    <li>All the material used are environmental friendly.</li>
  </ul>

  <p class="statement">We Do it all and much more!</p>
  <div class="rule-dotted rule-dotted--slogan"></div>
  <p class="slogan">Experience the Difference</p>
  <p class="disclaimer">*This opening offer will be limited time</p>

  <p class="address">
    <svg width="22" height="30" viewBox="0 0 22 30" aria-hidden="true"><path d="M11 0C5 0 0 5 0 11c0 8 11 19 11 19s11-11 11-19C22 5 17 0 11 0z" fill="#1f6db3"/><circle cx="11" cy="11" r="4" fill="#fff"/></svg>
    22 Marsa St. Ruwais
  </p>

  <div class="phone-line"></div>
  <p class="phone">
    <span class="phone__icon">
      <svg width="28" height="28" viewBox="0 0 24 24" aria-hidden="true"><path d="M6.6 10.8a15.1 15.1 0 006.6 6.6l2.2-2.2c.3-.3.7-.4 1-.2 1.1.4 2.3.6 3.6.6.6 0 1 .4 1 1V20c0 .6-.4 1-1 1A17 17 0 013 4c0-.6.4-1 1-1h3.5c.6 0 1 .4 1 1 0 1.3.2 2.5.6 3.6.1.3 0 .7-.2 1l-2.3 2.2z" fill="#1f6db3"/></svg>
    </span>
    5310 6648
  </p>

  <div class="duster" role="img" aria-label="Photo of a feather duster with a white handle"></div>

  <svg class="offer-badge" viewBox="0 0 320 320" aria-label="Opening offer 30% off">
    <defs>
      <path id="ring-path" d="M160 20 a140 140 0 1 1 -0.1 0"/>
      <radialGradient id="badge-fill" cx="40%" cy="35%" r="70%">
        <stop offset="0" stop-color="#3f9be0"/><stop offset="1" stop-color="#154f8e"/>
      </radialGradient>
    </defs>
    <path d="M160 20 a140 140 0 1 1 -140 140" fill="none" stroke="#8cc63f" stroke-width="30"/>
    <text font-family="Montserrat, sans-serif" font-weight="700" font-size="15" fill="#ffffff" letter-spacing="2">
      <textPath href="#ring-path" startOffset="2%">OPENING OFFER ... OPENING OFFER ...</textPath>
    </text>
    <circle cx="160" cy="160" r="112" fill="url(#badge-fill)"/>
    <text x="160" y="168" text-anchor="middle" font-family="Quicksand, sans-serif" font-weight="500" font-size="96" fill="#cfe6f8">30%</text>
    <text x="160" y="230" text-anchor="middle" font-family="Montserrat, sans-serif" font-weight="800" font-size="54" fill="#ffffff">OFF*</text>
  </svg>

  <div class="brand-mark">
    <span class="brand-mark__dot"></span>
    <span>Brisa Home</span>
  </div>
</main>
</body>
</html>
```